Tovin Marsk Technologies Web Site

I need website designed for Tovin Marsk Technologies, LLC. It is an email marketing software as a service business. I am looking for a five page website with the ability to accept payments. I have included our logo below for integration with the website. I do not have the text ready yet.

The domain to use is tovin-marsk.com

I have also included some examples of other websites that outline the basic structure I would like
https://trybluvesto.com/
https://www.postvaro.com/

I know I need to provide some more information, but I want to get the ball rolling and see what is needed.
Thanks!
Eli

```html
<!DOCTYPE html>
<html lang="en">
<head>
<meta charset="utf-8">
<title>Tovin Marsk Technologies</title>
<link href="https://fonts.googleapis.com/css2?family=Poppins:wght@400;500;600;700&display=swap" rel="stylesheet">
<style>
  :root {
    --navy: #1c1360;
    --blue: #2f5ee6;
    --ink: #1f1d4a;
    --muted: #9a9bbd;
    --soft: #f4f6fc;
    --white: #ffffff;
  }
  * { margin: 0; padding: 0; box-sizing: border-box; }
  html, body { width: 802px; height: 1200px; overflow: hidden; background: var(--white); }
  body { position: relative; font-family: "Poppins", sans-serif; color: var(--ink); }
  .bg { position: absolute; left: 0; top: 0; }
  .abs { position: absolute; }

  .brand { left: 78px; top: 36px; font-size: 12px; font-weight: 600; color: var(--white); line-height: 1; white-space: nowrap; }

  .nav { top: 18px; font-size: 8.5px; font-weight: 500; color: var(--white); }
  .nav-login { left: 650px; top: 12px; width: 101px; height: 23px; border-radius: 12px; background: var(--white); color: var(--blue); font-size: 8.5px; display: flex; align-items: center; justify-content: center; gap: 4px; }

  .hero-title { left: 0; width: 802px; top: 114px; text-align: center; color: var(--white); font-weight: 700; font-size: 37px; line-height: 44px; letter-spacing: -.5px; }
  .hero-text { left: 0; width: 802px; top: 207px; text-align: center; color: var(--white); font-size: 10px; line-height: 19px; }
  .btn-outline { top: 262px; height: 24px; border: 1px solid var(--white); border-radius: 12px; color: var(--white); font-size: 8px; font-weight: 500; display: flex; align-items: center; justify-content: center; }
  .scroll-down { left: 382px; top: 372px; width: 38px; height: 38px; border-radius: 50%; background: var(--blue); border: 2px solid var(--white); display: flex; align-items: center; justify-content: center; }

  .feature { top: 496px; width: 160px; }
  .feature svg { display: block; }
  .feature-rule { width: 30px; height: 1px; background: var(--blue); margin-top: 8px; }
  .feature h3 { font-size: 11px; font-weight: 500; margin-top: 16px; color: var(--ink); }
  .feature p { width: 152px; font-size: 7.2px; color: var(--muted); line-height: 15px; margin-top: 12px; }

  .section-title { left: 0; width: 802px; top: 722px; text-align: center; font-size: 18px; font-weight: 600; color: var(--ink); }
  .section-text { left: 0; width: 802px; top: 766px; text-align: center; font-size: 7.3px; color: var(--muted); line-height: 14.5px; }

  .plan { top: 828px; width: 162px; height: 288px; background: var(--white); overflow: hidden; box-shadow: 0 2px 10px rgba(28,19,96,.04); }
  .plan h4 { text-align: center; font-size: 11px; font-weight: 500; margin-top: 14px; }
  .plan .plan-sub { text-align: center; font-size: 7px; color: var(--muted); margin-top: 4px; }
  .plan .plan-rule { width: 30px; height: 1px; background: var(--blue); margin: 10px auto 0; }
  .plan ul { list-style: none; margin: 12px 0 0 18px; }
  .plan li { font-size: 7px; color: #7b7da3; line-height: 18.5px; }
  .price { margin: 10px 0 0 18px; font-size: 20px; color: var(--ink); font-weight: 400; line-height: 1; }
  .price sup { font-size: 8px; vertical-align: 10px; }
  .price sub { font-size: 7px; color: var(--muted); vertical-align: 0; }
  .plan-foot { position: absolute; left: 0; bottom: 0; width: 162px; height: 74px; }
  .buy { position: absolute; left: 46px; top: 247px; width: 70px; height: 23px; border: 1px solid var(--white); border-radius: 12px; color: var(--white); font-size: 7.8px; display: flex; align-items: center; justify-content: center; }
  .popular { position: absolute; left: 148px; top: 150px; width: 13px; height: 72px; background: var(--blue); color: var(--white); font-size: 6.5px; font-weight: 500; writing-mode: vertical-rl; transform: rotate(180deg); display: flex; align-items: center; justify-content: center; letter-spacing: .5px; }
</style>
</head>
<body>
  <svg class="bg" width="802" height="1200" viewBox="0 0 802 1200" aria-hidden="true">
    <polygon points="0,686 802,686 802,1075 0,1159" fill="var(--soft)"/>
    <polygon points="0,766 802,686 802,0 0,0" fill="var(--white)"/>
    <polygon points="0,0 802,0 802,350 0,433" fill="var(--navy)"/>
  </svg>

  <div class="abs" role="img" aria-label="Faint cloud and circuit decoration" style="left:666px;top:393px;width:136px;height:253px;background:linear-gradient(180deg,rgba(232,236,250,.55),rgba(240,243,252,.3));border-radius:60px 0 0 0;"></div>

  <div class="abs brand">Tovin Marsk</div>

  <div class="abs nav" style="left:298px">Solutions</div>
  <div class="abs nav" style="left:362px">Pricing</div>
  <div class="abs nav" style="left:416px">Tovin Marsk for ▾</div>
  <div class="abs nav" style="left:510px">Customers ▾</div>
  <div class="abs nav" style="left:589px">Resources</div>
  <div class="abs nav-login">
    <svg width="8" height="8" viewBox="0 0 10 10"><circle cx="7" cy="3" r="2.3" fill="none" stroke="currentColor" stroke-width="1.4"/><path d="M5.5 4.5 L1 9" stroke="currentColor" stroke-width="1.4"/></svg>Login
  </div>

  <h1 class="abs hero-title">Build Together<br>New Space for World</h1>
  <p class="abs hero-text">Sed ut perspiciatis unde omnis iste natus error sit voluptatem ccusantium doloremque<br>laudantium, totam rem aperiam inventore.</p>
  <div class="abs btn-outline" style="left:304px;width:98px">Check Features</div>
  <div class="abs btn-outline" style="left:411px;width:87px">Explore More</div>
  <div class="abs scroll-down">
    <svg width="10" height="10" viewBox="0 0 10 10"><path d="M5 1 V8 M2 5.5 L5 8.5 L8 5.5" stroke="#fff" stroke-width="1.4" fill="none"/></svg>
  </div>

  <div class="abs feature" style="left:50px">
    <svg width="36" height="36" viewBox="0 0 36 36" fill="none" stroke="var(--blue)" stroke-width="1.3"><circle cx="18" cy="18" r="17"/><circle cx="18" cy="18" r="13"/><path d="M18 18 L24 10"/><circle cx="18" cy="18" r="2"/></svg>
    <div class="feature-rule"></div>
    <h3>High Performance</h3>
    <p>Sed ut perspiciatis unde omnis isterror<br>sit accusantium</p>
  </div>
  <div class="abs feature" style="left:230px">
    <svg width="36" height="36" viewBox="0 0 36 36" fill="none" stroke="var(--blue)" stroke-width="1.3"><path d="M4 24 A15 15 0 1 1 14 33"/><path d="M10 32 L14 33 L12 29"/><rect x="12" y="15" width="12" height="10" rx="1"/><path d="M14 15 V11 a4 4 0 0 1 8 0 V15"/><circle cx="18" cy="20" r="1.3"/></svg>
    <div class="feature-rule"></div>
    <h3>Enhance Security</h3>
    <p>Sed ut perspiciatis unde omnis isterror<br>sit accusantium</p>
  </div>
  <div class="abs feature" style="left:410px">
    <svg width="36" height="36" viewBox="0 0 36 36" fill="none" stroke="var(--blue)" stroke-width="1.3"><path d="M18 2 L32 7 V18 C32 26 25 31 18 34 C11 31 4 26 4 18 V7 Z"/><circle cx="18" cy="15" r="4"/><path d="M11 26 C12 21 24 21 25 26"/></svg>
    <div class="feature-rule"></div>
    <h3>Spam Guard</h3>
    <p>Sed ut perspiciatis unde omnis isterror<br>sit accusantium</p>
  </div>
  <div class="abs feature" style="left:589px">
    <svg width="36" height="36" viewBox="0 0 36 36" fill="none" stroke="var(--blue)" stroke-width="1.3"><path d="M6 4 L12 10 L10 12 L4 6 Z M11 11 L30 30 L28 32 L9 13"/><path d="M30 4 a6 6 0 0 0 -7 8 L6 29 L8 31 L25 14 a6 6 0 0 0 8 -7 L29 11 L26 8 Z"/></svg>
    <div class="feature-rule"></div>
    <h3>Unbeatable Support</h3>
    <p>Sed ut perspiciatis unde omnis isterror<br>sit accusantium</p>
  </div>

  <h2 class="abs section-title">Our Pricing Plan</h2>
  <p class="abs section-text">There are many variations of passages of Lorem Ipsum available, but the majority have<br>suffered alteration in some form, by injected humour</p>

  <div class="abs plan" style="left:50px">
    <h4>Basic</h4><p class="plan-sub">Put some text here</p><div class="plan-rule"></div>
    <ul><li>RAM 1 GB</li><li>Core CPU 1</li><li>SSD Storage 20 GB</li><li>Transfer 1 TB</li><li>Network In 40 Gbps</li><li>Network Out 1000 Mbps</li></ul>
    <div class="price"><sup>$</sup>29<sub>M</sub></div>
    <svg class="plan-foot" viewBox="0 0 162 74"><polygon points="0,13 162,0 162,74 0,74" fill="var(--navy)"/></svg>
    <div class="buy">Buy Now</div>
  </div>
  <div class="abs plan" style="left:230px">
    <h4>Standard</h4><p class="plan-sub">Put some text here</p><div class="plan-rule"></div>
    <ul><li>RAM 1 GB</li><li>Core CPU 1</li><li>SSD Storage 20 GB</li><li>Transfer 1 TB</li><li>Network In 40 Gbps</li><li>Network Out 1000 Mbps</li></ul>
    <div class="price"><sup>$</sup>47<sub>M</sub></div>
    <div class="popular">Most popular</div>
    <svg class="plan-foot" viewBox="0 0 162 74"><polygon points="0,0 162,13 162,74 0,74" fill="var(--navy)"/></svg>
    <div class="buy">Buy Now</div>
  </div>
  <div class="abs plan" style="left:410px">
    <h4>Professional</h4><p class="plan-sub">Put some text here</p><div class="plan-rule"></div>
    <ul><li>RAM 1 GB</li><li>Core CPU 1</li><li>SSD Storage 20 GB</li><li>Transfer 1 TB</li><li>Network In 40 Gbps</li><li>Network Out 1000 Mbps</li></ul>
    <div class="price"><sup>$</sup>59<sub>M</sub></div>
    <svg class="plan-foot" viewBox="0 0 162 74"><polygon points="0,13 162,0 162,74 0,74" fill="var(--navy)"/></svg>
    <div class="buy">Buy Now</div>
  </div>
  <div class="abs plan" style="left:589px">
    <h4>Business</h4><p class="plan-sub">Put some text here</p><div class="plan-rule"></div>
    <ul><li>RAM 1 GB</li><li>Core CPU 1</li><li>SSD Storage 20 GB</li><li>Transfer 1 TB</li><li>Network In 40 Gbps</li><li>Network Out 1000 Mbps</li></ul>
    <div class="price"><sup>$</sup>180<sub>M</sub></div>
    <svg class="plan-foot" viewBox="0 0 162 74"><polygon points="0,0 162,13 162,74 0,74" fill="var(--navy)"/></svg>
    <div class="buy">Buy Now</div>
  </div>
</body>
</html>
```